Business Card - high end, modern health care

Hey designers!

We need a double sided business card for the boutique, cutting edge physical therapy rehabilitation centre in Sydney's Northern Beaches.

With the most qualified physios in the area The Harbourline Motion Clinic does what other physiotherapy practices do not, we take our time with our patients giving them longer appointments, better physios and therefor faster results!

We guarantee that the service people receive at THMC will be unparalleled.

Hence we need a business card to reflect our modern, boutique, high end service. The final design needs to reflect that we are in a class of our own yet with the feel of beachside retreat.

Below I have attached our logo in both blue on white and white on blue. The exact colour is;
and the font that we have used in our logo is Tex Gyre Aventador.

I like the idea of the blue as the main colour as it is more eye catching and our signage onto the main road will be in this blue and in the interest of consistency across marketing the blue needs to be a part of the design. However I would appreciate a few designs onto a wooden background as this is a visual theme within the fitout of the practice.

The design needs to be of standard size (91x55mm).

Target Market(s)

We target people who have an end outcome in mind and those who have had poor experiences with other providers and ensure that everyone gets the care that they deserve with a premium service that is tailored to the individuals circumstances. As a premium service, the target market is highly educated, business and tech savvy with the additional target market of elderly people who have self funded their retirement and see value in paying for the best ongoing rehabilitation to maintain independence.

Industry/Entity Type

Physical Therapy

Contact Information for Business Card

Name, designation( Titled Musculoskeletal Physiotherapist... there will also be those in the company that have multiple designations ie 5 or 6 words long), phone number, email, facebook, instagram, address

Font styles to use
Sans Serif

Colors

Designer to choose colors to be used in the design.

Requirements
Must have
• Front - The logo as large as possible, blue or wooden theme, and all of the important details.
• Back - A blank space/lines on which to write appointment times (no "Appointment, date, time" etc.)
Nice to have
• facebook url
• logos for facebook and instagram
• Mini logos for the phone and email?

```html
<!DOCTYPE html>
<html lang="en">
<head>
<meta charset="utf-8">
<title>The Harbourline Motion Clinic – Business Card</title>
<link rel="stylesheet" href="https://fonts.googleapis.com/css2?family=Work+Sans:wght@400;500&display=swap">
<style>
  :root {
    --stage: #2b2b2d;
    --brand-blue: #1257a8;
    --silver: #d3dbe6;
    --paper: #ffffff;
    --ink-blue: #1a56b0;
  }
  * { box-sizing: border-box; margin: 0; padding: 0; }
  html, body { width: 1200px; height: 900px; overflow: hidden; }
  body {
    background: var(--stage);
    font-family: "Work Sans", Arial, sans-serif;
    position: relative;
  }
  .card {
    position: absolute;
    left: 290px;
    width: 620px;
    height: 375px;
    overflow: hidden;
    box-shadow: 0 10px 24px rgba(0,0,0,.45);
  }
  /* Appointment side */
  .card--back { top: 45px; background: var(--paper); }
  .card--back .band {
    height: 118px;
    background: var(--brand-blue);
    display: flex;
    align-items: center;
    justify-content: center;
  }
  .wordmark {
    color: var(--silver);
    font-weight: 500;
    text-transform: uppercase;
    line-height: 1;
    white-space: nowrap;
  }
  .wordmark .line-1 { display: block; font-size: 30px; letter-spacing: 1px; }
  .wordmark .line-2 { display: block; font-size: 17px; letter-spacing: 7.5px; margin-top: 6px; }
  .card--back .wordmark { text-align: center; }
  .appointment {
    display: block;
    width: max-content;
    margin: 38px auto 0;
    color: var(--ink-blue);
    font-size: 19px;
    letter-spacing: 1px;
    padding-bottom: 3px;
    border-bottom: 1.5px solid var(--ink-blue);
  }
  /* Contact side */
  .card--front { top: 480px; background: var(--brand-blue); }
  .brand {
    position: absolute;
    left: 28px;
    top: 150px;
    display: flex;
    align-items: center;
    gap: 10px;
  }
  .brand .mark-dot {
    width: 42px; height: 42px;
    border-radius: 50%;
    border: 2px solid var(--silver);
    flex: none;
  }
  .brand .wordmark .line-1 { font-size: 21px; letter-spacing: .6px; }
  .brand .wordmark .line-2 { font-size: 13px; letter-spacing: 4.6px; }
  .divider {
    position: absolute;
    left: 334px;
    top: 80px;
    width: 1.5px;
    height: 180px;
    background: var(--silver);
    opacity: .85;
  }
  .details {
    position: absolute;
    left: 356px;
    top: 84px;
    right: 18px;
    color: var(--silver);
    white-space: nowrap;
  }
  .person-name { font-size: 22px; font-weight: 500; letter-spacing: .5px; text-transform: uppercase; }
  .person-role { font-size: 14px; letter-spacing: .8px; margin-top: 2px; }
  .address { font-size: 14px; line-height: 1.45; letter-spacing: .3px; margin-top: 18px; }
  .contact-list { list-style: none; margin-top: 14px; font-size: 14px; letter-spacing: .3px; }
  .contact-list li { display: flex; align-items: center; gap: 9px; line-height: 1.6; }
  .contact-list svg { width: 12px; height: 12px; flex: none; }
  .social {
    position: absolute;
    left: 440px;
    top: 318px;
    display: flex;
    gap: 14px;
  }
  .social span { width: 14px; height: 14px; border: 1.5px solid var(--silver); border-radius: 3px; }
</style>
</head>
<body>
  <section class="card card--back" aria-label="Appointment side">
    <div class="band">
      <p class="wordmark"><span class="line-1">The Harbourline</span><span class="line-2">Motion Clinic</span></p>
    </div>
    <p class="appointment">Appointment:</p>
  </section>

  <section class="card card--front" aria-label="Contact side">
    <div class="brand">
      <span class="mark-dot"></span>
      <p class="wordmark"><span class="line-1">The Harbourline</span><span class="line-2">Motion Clinic</span></p>
    </div>
    <div class="divider"></div>
    <div class="details">
      <h1 class="person-name">Daniel Reyes</h1>
      <p class="person-role">Director</p>
      <p class="address">27 Tidewater Lane, Unit 4,<br>Marlow Bay, PO 20418</p>
      <ul class="contact-list">
        <li><svg viewBox="0 0 12 12" aria-hidden="true"><path d="M2.5 1h2l1 2.6-1.3 1a6 6 0 0 0 3.2 3.2l1-1.3L11 7.5v2A1.5 1.5 0 0 1 9.5 11 8.5 8.5 0 0 1 1 2.5 1.5 1.5 0 0 1 2.5 1z" fill="none" stroke="#d3dbe6" stroke-width="1"/></svg>+330 5871-2043</li>
        <li><svg viewBox="0 0 12 12" aria-hidden="true"><rect x="1" y="2.5" width="10" height="7" fill="none" stroke="#d3dbe6" stroke-width="1"/><path d="M1 2.5l5 4 5-4" fill="none" stroke="#d3dbe6" stroke-width="1"/></svg>info@harbourlinemotion.com</li>
        <li><svg viewBox="0 0 12 12" aria-hidden="true"><circle cx="6" cy="6" r="5" fill="none" stroke="#d3dbe6" stroke-width="1"/><ellipse cx="6" cy="6" rx="2.2" ry="5" fill="none" stroke="#d3dbe6" stroke-width="1"/><path d="M1 6h10" stroke="#d3dbe6" stroke-width="1"/></svg>www.harbourlinemotion.com</li>
      </ul>
    </div>
    <div class="social" aria-hidden="true"><span></span><span></span></div>
  </section>
</body>
</html>
```